Political Association Member Newsletter

We require a professional newsletter designed that will be sent both by mail and by email (and can be posted online) to the members in our client organization. I will develop and curate the content to send to the designer but we need help with a good design.

We have two key colours: red and blue (usually on white background). The pantones are:
blue = 301C
red = 032C

The logo I have from the client is attached as well as a recent piece with contact information and social media channels noted.

The client also provided a campaign logo "Raise the Bar for 2019" that will accompany copy for membership and donation which will follow.

Two preliminary content pieces are also included here: a flyer for a bbq and the "Regional Forum Digest" article.

Political

Sans Serif

• Space for pictures - uploaded below.

```html
<!DOCTYPE html>
<html lang="en">
<head>
<meta charset="utf-8">
<title>Riverside Centre Member Newsletter</title>
<link rel="stylesheet" href="https://fonts.googleapis.com/css2?family=Arimo:wght@400;700&family=Open+Sans:wght@600;700&display=swap">
<style>
  :root {
    --brand-blue: #1a4d86;
    --brand-red: #d22b26;
    --page-grey: #f2f2f2;
    --ink: #1f1f1f;
    --caption-grey: #5a5a5a;
    --social-blue: #2fa3dc;
    --social-navy: #3b5590;
    --photo-warm: #8a7a66;
    --photo-hall: #2a2f5a;
  }
  * { margin: 0; padding: 0; box-sizing: border-box; }
  html, body { width: 1200px; height: 3750px; overflow: hidden; }
  body { background: var(--page-grey); font-family: "Arimo", Arial, sans-serif; color: var(--ink); position: relative; }
  .abs { position: absolute; }

  .top-rule { left: 0; top: 0; width: 1200px; height: 12px; background: var(--brand-red); }
  .masthead { left: 0; top: 12px; width: 1200px; height: 138px; background: #fff; }
  .brand { left: 60px; top: 52px; display: flex; align-items: center; gap: 20px; }
  .brand-dot { width: 62px; height: 62px; border-radius: 50%; background: var(--brand-blue); }
  .brand-name { font-family: "Open Sans", sans-serif; font-weight: 700; font-size: 24px; line-height: 28px; color: var(--brand-blue); }
  .issue-date { right: 105px; top: 92px; font-family: "Open Sans", sans-serif; font-weight: 700; font-size: 22px; color: var(--brand-blue); }
  .band { left: 0; top: 155px; }

  .photo { background: linear-gradient(160deg, #b9aa92, var(--photo-warm) 55%, #4b4137); }
  .photo-lead { left: 270px; top: 275px; width: 870px; height: 500px; }
  .caption { font-family: "Open Sans", sans-serif; font-weight: 700; font-size: 16px; line-height: 25px; color: var(--caption-grey); text-transform: uppercase; }
  .caption-lead { left: 270px; top: 795px; width: 870px; text-align: center; }

  .article-title { left: 0; top: 900px; width: 1200px; text-align: center; font-weight: 700; font-size: 36px; }
  .article-body { left: 60px; top: 958px; width: 1080px; font-size: 34px; line-height: 42px; }
  .article-body p { margin-bottom: 40px; }

  .signature { right: 60px; top: 2040px; text-align: right; font-weight: 700; font-size: 34px; line-height: 49px; }
  .signature .sig-email { color: var(--brand-red); }

  .button { display: flex; align-items: center; justify-content: center; font-family: "Open Sans", sans-serif; font-weight: 700; color: #fff; text-transform: uppercase; }
  .button-blue { background: var(--brand-blue); }
  .button-red { background: var(--brand-red); }
  .contact-button { left: 945px; top: 2188px; width: 195px; height: 70px; font-size: 26px; }

  .photo-hall { background: linear-gradient(170deg, #4a5aa0, var(--photo-hall) 55%, #141628); }
  .photo-delegates { left: 60px; top: 2375px; width: 512px; height: 545px; }
  .photo-stage { left: 618px; top: 2375px; width: 522px; height: 355px; }
  .caption-stage { left: 618px; top: 2748px; width: 522px; }
  .see-more { left: 618px; top: 2850px; width: 215px; height: 70px; font-size: 26px; }
  .caption-delegates { left: 60px; top: 2950px; width: 512px; }

  .renew-button { left: 325px; top: 3120px; width: 540px; height: 66px; font-size: 25px; }

  .social { top: 3268px; display: flex; align-items: center; gap: 22px; font-family: "Open Sans", sans-serif; font-weight: 700; font-size: 29px; }
  .social-dot { width: 63px; height: 63px; border-radius: 50%; }
  .social-x { left: 60px; color: var(--social-blue); }
  .social-x .social-dot { background: var(--social-blue); }
  .social-page { left: 488px; color: var(--social-navy); }
  .social-page .social-dot { background: var(--social-navy); }

  .footer { left: 0; top: 3388px; width: 1200px; height: 330px; background: var(--brand-blue); color: #fff; }
  .footer-col { top: 64px; font-size: 27px; line-height: 48px; }
  .footer-left { left: 60px; }
  .footer-right { right: 60px; text-align: right; }
  .footer-rule { left: 60px; top: 264px; width: 1080px; height: 2px; background: rgba(255,255,255,0.55); }
  .footer-legal { top: 280px; font-size: 24px; }
  .footer-legal-left { left: 60px; }
  .footer-legal-right { right: 60px; }
  .footer-legal-right .unsubscribe { color: var(--brand-red); }
  .bottom-rule { left: 0; top: 3718px; width: 1200px; height: 32px; background: var(--brand-red); }
</style>
</head>
<body>
  <div class="abs top-rule"></div>
  <header class="abs masthead"></header>
  <div class="abs brand">
    <span class="brand-dot"></span>
    <span class="brand-name">Civic Alliance Party,<br>Riverside Centre</span>
  </div>
  <div class="abs issue-date">Saturday July 23,2016</div>
  <svg class="abs band" width="1200" height="40" viewBox="0 0 1200 40">
    <polygon points="0,0 592,0 578,40 0,40" fill="var(--brand-red)"/>
    <polygon points="606,0 1200,0 1200,40 592,40" fill="var(--brand-blue)"/>
  </svg>

  <div class="abs photo photo-lead" role="img" aria-label="Photo of three party members standing together at the annual general meeting"></div>
  <div class="abs caption caption-lead">Hon. Gordon Pell along with R.T. Madsen and Owen<br>Farrow at the Alliance AGM in Harbourview</div>

  <h1 class="abs article-title">Regional Forum Digest: Daniel Korvath</h1>
  <div class="abs article-body">
    <p>&nbsp;It’s my pleasure to introduce myself as the newest member of National Council from the Northern Region. I will join Renata Olsen from Westbrook representing the views of members from across the province. I’ve met many of you over the years, in particular during my three years as EDA President in Riverside Centre, and I’m looking forward to working for you again.</p>
    <p>&nbsp;The 2016 Alliance National Convention was a remarkable success. Our Party took important steps toward building a foundation for a broader coalition of members, we said thank you to former Prime Minister Martin Caldwell, and we heard compelling narratives for what lies ahead.</p>
    <p>We also elected Trevor Banks as our new Party President. Trevor is a Harbourview-based lawyer with a keen sense of the issues that need to be addressed in the months ahead. I trust you’ll join me in congratulating Trevor!</p>
    <p>I know many of you have a busy summer ahead, but I encourage you to stay engaged with your EDA and our Party. Join us at the Northern Region Alliance BBQ on August 13, volunteer for a leadership campaign, or encourage your neighbours to become members and join our team. Together we can put our Party in a position to bring better government back to our great country!</p>
  </div>

  <div class="abs signature">
    Daniel Korvath<br>National Council<br><span class="sig-email">dkorvath@civicalliance.org</span>
  </div>
  <div class="abs button button-blue contact-button">Contact Me</div>

  <div class="abs photo-hall photo-delegates" role="img" aria-label="Photo of Riverside Centre delegates seated at a long table at the convention"></div>
  <div class="abs photo-hall photo-stage" role="img" aria-label="Photo of a large convention hall with a speaker on stage before thousands of delegates"></div>
  <div class="abs caption caption-stage">Thousands gathered as Hon. Elise Marchand,<br>interim leader, addresses the delegates.</div>
  <div class="abs button button-blue see-more">See More</div>
  <div class="abs caption caption-delegates">Riverside Centre delegates working hard<br>at the convention.</div>

  <div class="abs button button-red renew-button">Renew your membership today!</div>

  <div class="abs social social-x"><span class="social-dot"></span>@RiversideCAP</div>
  <div class="abs social social-page"><span class="social-dot"></span>Riverside Centre Civic Association</div>

  <footer class="abs footer">
    <div class="abs footer-col footer-left">Address :<br>Northern Region Area Office<br>#210, 4820 Lakeview Rd<br>Riverside, NR R2B 4K7</div>
    <div class="abs footer-col footer-right">Phone: 555-014-2290<br>555-014-3817<br>Fax : 555-014-6650<br>E-mail : info@civicalliance.org</div>
    <div class="abs footer-rule"></div>
    <div class="abs footer-legal footer-legal-left">This is E-mail 2016. All Rights Reserved.</div>
    <div class="abs footer-legal footer-legal-right">View This E-mail Online &nbsp;|&nbsp; <span class="unsubscribe">Unsubscribe</span></div>
  </footer>
  <div class="abs bottom-rule"></div>
</body>
</html>
```